Web Design Project

We are a business based in Sydney Australia, we have a very cool and sophisticated AI platform that lets you create Virtual Agents mainly for Enterprise clients but we are now moving into the Personal AI space where we will have mobile apps using our technology. We need a new look and feel with some better branding

We will progress this in stages with a quick touch up to our site followed by a more thorough rebuild.

So for now, on our web site, stage 1.... I'm happy to change colours, we will keep the "head" in our logo but change our name. if you look at out site at www.mylumenfold.example you will see that there is content but not much structure...we will include videos at some point and some infographics but not just yet ....so I'm after a suite of 3 different template designs that we can use and I want to work with the successful designer to tweak them and populate them with a lot of our current content.

We will keep our avatar but she may need a makeover...I'm open to suggestions on how to make our site more progressive. Would a more tiled, panelos 5 look and feel work?

I would prefer to use word press

Target Market(s)

mainly enterprise clients, big banks, insurance companies, telcos

Industry/Entity Type

Business

Requirements
Nice to have
• check out some of our competitors....brivoQA, TelmaRi, amber lattice, dorvaspark, quarnoreply, hOlpa

I was thinking that a more tiled 'panelos 5' look and feel might be good...open to suggestions
Should not have
• can't look cheap and nasty

```html
<!DOCTYPE html>
<html lang="en">
<head>
<meta charset="utf-8">
<title>MyLumenfold — Home</title>
<link rel="stylesheet" href="https://fonts.googleapis.com/css2?family=PT+Sans+Narrow:wght@400;700&display=swap">
<style>
:root{
  --ink:#222;
  --header-top:#ffffff;
  --header-bottom:#dcdcdc;
  --nav-active:#52b4a1;
  --nav-a:#2f6f62;
  --nav-b:#367d6f;
  --nav-band:#2b6357;
  --stage:#1b1b1b;
  --stage-mark:#3a3a3a;
  --tile-intro:#2f2f2f;
  --tile-1:#4b4b4b;
  --tile-2:#6a6a6a;
  --tile-3:#9b9b9b;
  --tile-4:#5e5e5e;
  --tile-5:#8a8a8a;
  --tile-6:#b7b7b7;
  --icon-light:#d9d9d9;
  --link:#f5b21b;
  --cta-orange:#ff6a14;
  --cta-yellow:#ffe400;
  --cta-teal:#0a8b96;
  --cta-cyan:#27c4ef;
  --white:#ffffff;
}
*{margin:0;padding:0;box-sizing:border-box}
html,body{width:1200px;height:1155px;overflow:hidden;background:var(--white)}
body{position:relative;font-family:"PT Sans Narrow",sans-serif;color:var(--ink)}
.site-header{position:absolute;left:101px;top:0;width:999px;height:115px;
  background:linear-gradient(180deg,var(--header-top) 0%,var(--header-top) 40%,var(--header-bottom) 100%)}
.site-header .login-zone{position:absolute;right:0;top:0;width:165px;height:115px;
  background:linear-gradient(180deg,#fff 0%,#fff 60%,#ececec 100%)}
.brand{position:absolute;left:40px;top:38px;display:flex;align-items:center;gap:12px}
.brand-name{font-size:46px;letter-spacing:3px;color:#1c1c1c;font-weight:400;line-height:1}
.brand-dot{width:34px;height:34px;border-radius:50%;background:var(--nav-b)}
.login{position:absolute;left:910px;top:77px;display:flex;align-items:center;gap:4px;font-size:15px;color:#333}
.main-nav{position:absolute;left:101px;top:115px;width:999px;height:128px;display:flex;border-bottom:6px solid var(--nav-band)}
.nav-item{height:122px;color:var(--white);text-align:center;font-size:18px;padding-top:11px;position:relative}
.nav-item svg,.nav-item .icon-ph{display:block;margin:14px auto 0}
.nav-item:nth-child(odd){background:var(--nav-b)}
.nav-item:nth-child(even){background:var(--nav-a)}
.nav-item.is-active{background:var(--nav-active)}
.nav-item.is-active::after{content:"";position:absolute;left:67px;top:128px;border:9px solid transparent;border-top-color:var(--nav-band)}
.icon-ph{border-radius:6px}
.stage{position:absolute;left:101px;top:243px;width:999px;height:357px;background:var(--stage)}
.stage-play{position:absolute;left:476px;top:134px}
.stage-name{position:absolute;left:0;width:100%;top:210px;text-align:center;font-size:44px;letter-spacing:4px;color:var(--stage-mark)}
.intro{position:absolute;left:101px;top:600px;width:250px;height:333px;background:var(--tile-intro);color:var(--white);padding:20px 28px 0 21px}
.intro h2{font-size:17px;font-weight:400;line-height:18px;width:140px}
.intro .globe{position:absolute;left:176px;top:16px}
.intro p{margin-top:28px;font-size:13.4px;line-height:18px;text-align:justify;color:#e8e8e8}
.intro a{color:var(--link);text-decoration:none}
.tile{position:absolute;width:250px;height:167px;color:var(--white);text-align:center;font-size:17px;line-height:18px;padding-top:20px}
.tile svg,.tile .icon-ph{display:block;margin:16px auto 0}
.t1{left:351px;top:600px;background:var(--tile-1)}
.t2{left:601px;top:600px;background:var(--tile-2)}
.t3{left:851px;top:600px;background:var(--tile-3)}
.t4{left:351px;top:767px;height:166px;background:var(--tile-4)}
.t5{left:601px;top:767px;height:166px;background:var(--tile-5)}
.t6{left:851px;top:767px;height:166px;background:var(--tile-6)}
.cta{position:absolute;top:933px;height:94px;display:flex;align-items:center;color:var(--white)}
.cta-free{left:101px;width:500px;background:var(--cta-orange);padding-left:22px;font-size:17px}
.cta-free strong{color:var(--cta-yellow);font-size:25px;font-weight:400;margin-left:4px}
.cta-personal{left:601px;width:500px;background:var(--cta-teal);justify-content:center;font-size:17px}
.cta-personal strong{color:var(--cta-cyan);font-size:27px;font-weight:400;margin-left:5px}
.social{position:absolute;left:114px;top:1056px;display:flex;gap:5px;list-style:none}
.social li{width:39px;height:39px;border-radius:50%}
.social .s1{background:#3b5a9a}.social .s2{background:#33b4e8}.social .s3{background:#2a8fc4}
.social .s4{background:#f26b1d}.social .s5{background:#dcae6e}
.footer-brand{position:absolute;left:886px;top:1060px;display:flex;align-items:center;gap:6px}
.footer-brand span{font-size:22px;letter-spacing:2px;color:#1c1c1c}
.footer-brand i{width:18px;height:18px;border-radius:50%;background:var(--nav-b)}
.copyright{position:absolute;left:883px;top:1100px;font-size:14px;color:#222}
.page-code{position:absolute;left:1126px;top:1071px;font-size:14px;color:#222}
</style>
</head>
<body>
<header class="site-header">
  <div class="login-zone"></div>
  <div class="brand"><span class="brand-name">myLUMENFOLD</span><span class="brand-dot"></span></div>
  <div class="login">
    <svg width="18" height="21" viewBox="0 0 18 21"><path d="M4 9V6a5 5 0 0 1 10 0" fill="none" stroke="#333" stroke-width="2.4"/><rect x="1" y="9" width="16" height="12" rx="1.5" fill="#333"/><rect x="8" y="13" width="2" height="4" fill="#fff"/></svg>
    LOGIN
    <svg width="14" height="8" viewBox="0 0 14 8"><path d="M1 1h12L7 7z" fill="#555"/></svg>
  </div>
</header>

<nav class="main-nav">
  <div class="nav-item is-active" style="width:167px">HOME
    <svg width="66" height="56" viewBox="0 0 66 56"><path d="M4 28 33 4l29 24" fill="none" stroke="#fff" stroke-width="6" stroke-linejoin="round"/><path d="M12 27 33 10l21 17v27H40V38H26v16H12z" fill="#fff"/></svg>
  </div>
  <div class="nav-item" style="width:166px">TECHNOLOGY
    <svg width="62" height="60" viewBox="0 0 62 60"><g stroke="#fff" stroke-width="4" stroke-linecap="round"><path d="M31 2v8M9 12l6 5M53 12l-6 5M2 33h8M52 33h8M11 51l5-5M51 51l-5-5"/></g><circle cx="31" cy="31" r="12" fill="#fff"/><rect x="25" y="40" width="12" height="14" rx="2" fill="#fff"/></svg>
  </div>
  <div class="nav-item" style="width:167px">PRODUCTS
    <svg width="66" height="60" viewBox="0 0 66 60"><path d="M4 14 33 3l29 11v32L33 57 4 46z" fill="#fff"/><path d="M4 14l29 11 29-11M33 25v32" fill="none" stroke="#2f6f62" stroke-width="3"/><path d="M14 28v12M18 28v12M11 31l5-4 5 4" fill="none" stroke="#2f6f62" stroke-width="2"/></svg>
  </div>
  <div class="nav-item" style="width:167px">OUR LUMENFOLDS
    <div class="icon-ph" role="img" aria-label="Product head symbol" style="width:58px;height:60px;background:#5aa595;border-radius:50%"></div>
  </div>
  <div class="nav-item" style="width:167px">NEWS
    <div class="icon-ph" role="img" aria-label="Support agent with headset" style="width:64px;height:62px;background:#5aa595"></div>
  </div>
  <div class="nav-item" style="width:165px">COMPANY
    <svg width="64" height="62" viewBox="0 0 64 62"><path d="M2 20h28v42H2zM32 10l30-8v60H32z" fill="#fff"/><g fill="#2f6f62"><rect x="7" y="26" width="6" height="6"/><rect x="18" y="26" width="6" height="6"/><rect x="7" y="37" width="6" height="6"/><rect x="18" y="37" width="6" height="6"/><rect x="7" y="48" width="6" height="6"/><rect x="18" y="48" width="6" height="6"/><rect x="38" y="16" width="6" height="6"/><rect x="50" y="13" width="6" height="6"/><rect x="38" y="28" width="6" height="6"/><rect x="50" y="28" width="6" height="6"/><rect x="38" y="40" width="6" height="6"/><rect x="50" y="40" width="6" height="6"/></g></svg>
  </div>
</nav>

<section class="stage" aria-label="Introductory video">
  <svg class="stage-play" width="48" height="62" viewBox="0 0 48 62"><path d="M4 3h28l13 13v42H4z" fill="none" stroke="#5a5a5a" stroke-width="5" stroke-linejoin="round"/><path d="M18 21l16 10-16 10z" fill="#5a5a5a"/></svg>
  <div class="stage-name">myLUMENFOLD</div>
</section>

<section class="intro">
  <h2>OUR ENTERPRISE CUSTOMERS</h2>
  <svg class="globe" width="44" height="44" viewBox="0 0 44 44"><g fill="none" stroke="#bdbdbd" stroke-width="3"><circle cx="22" cy="22" r="19"/><ellipse cx="22" cy="22" rx="8" ry="19"/><path d="M3 22h38M6 12h32M6 32h32M22 3v38"/></g></svg>
  <p>MyLumenfold specializes in large enterprises with high compliance and security needs such as financial services, government and IT. The sector demands absolute accuracy, perfect legal compliance, high performance and robust security. MyLumenfold has the most extensive portfolio of financial services clients for high-end virtual agents, and has substantial experience and significant performance results in this sector. <a href="#">[Case Studies]</a></p>
</section>

<article class="tile t1">ARTIFICIAL INTELLIGENCE<br>FOR CUSTOMER SUPPORT
  <div class="icon-ph" role="img" aria-label="Person with approval tick" style="width:56px;height:56px;background:#8a8a8a"></div>
</article>
<article class="tile t2">HEALTH COACH
  <svg width="64" height="58" viewBox="0 0 64 58"><path d="M32 56 6 30A16 16 0 0 1 32 8a16 16 0 0 1 26 22z" fill="#d4d4d4"/><path d="M2 30h16l5-10 7 22 6-28 5 16h21" fill="none" stroke="#6a6a6a" stroke-width="3"/></svg>
</article>
<article class="tile t3">ENTERPRISE
  <svg width="72" height="58" viewBox="0 0 72 58"><rect x="10" y="3" width="52" height="40" rx="2" fill="none" stroke="#e6e6e6" stroke-width="3"/><path d="M2 46h68l-4 8H6z" fill="#e6e6e6"/><circle cx="36" cy="20" r="8" fill="none" stroke="#e6e6e6" stroke-width="2.5"/><path d="M36 22v14" stroke="#e6e6e6" stroke-width="2.5"/></svg>
</article>
<article class="tile t4">SMALL BUSINESS SOLUTIONS
  <svg width="82" height="80" viewBox="0 0 82 80"><g fill="#b8b8b8"><circle cx="26" cy="54" r="16"/><circle cx="58" cy="18" r="12"/><g transform="translate(26 54)"><rect x="-5" y="-25" width="10" height="50"/><rect x="-5" y="-25" width="10" height="50" transform="rotate(45)"/><rect x="-5" y="-25" width="10" height="50" transform="rotate(90)"/><rect x="-5" y="-25" width="10" height="50" transform="rotate(135)"/></g><g transform="translate(58 18)"><rect x="-4" y="-18" width="8" height="36"/><rect x="-4" y="-18" width="8" height="36" transform="rotate(45)"/><rect x="-4" y="-18" width="8" height="36" transform="rotate(90)"/><rect x="-4" y="-18" width="8" height="36" transform="rotate(135)"/></g></g><circle cx="26" cy="54" r="6" fill="#5e5e5e"/><circle cx="58" cy="18" r="5" fill="#5e5e5e"/></svg>
</article>
<article class="tile t5">SMALL BUSINESS SOLUTIONS
  <svg width="58" height="58" viewBox="0 0 58 58"><g fill="#d0d0d0"><rect x="2" y="36" width="14" height="20" rx="1"/><rect x="21" y="24" width="14" height="32" rx="1"/><rect x="40" y="10" width="14" height="46" rx="1"/><path d="M4 20 16 8l-4-4h12v12l-4-4L8 24z"/></g></svg>
</article>
<article class="tile t6">PROFESSIONAL
  <div class="icon-ph" role="img" aria-label="Business professional" style="width:56px;height:66px;background:#d6d6d6"></div>
</article>

<a class="cta cta-free" href="#">SIGN UP TODAY AND MAKE YOUR OWN LUMENFOLD FOR <strong>FREE!</strong></a>
<a class="cta cta-personal" href="#">PERSONAL - <strong>FREE REGISTRATION</strong></a>

<ul class="social" aria-label="Social links">
  <li class="s1" role="img" aria-label="Social network"></li>
  <li class="s2" role="img" aria-label="Social network"></li>
  <li class="s3" role="img" aria-label="Social network"></li>
  <li class="s4" role="img" aria-label="News feed"></li>
  <li class="s5" role="img" aria-label="Email"></li>
</ul>
<div class="footer-brand"><span>myLUMENFOLD</span><i></i></div>
<p class="copyright">© 2013.www.mylumenfold.example</p>
<p class="page-code">M1</p>
</body>
</html>
```